Business card alterations

I have changed my business name from Brisa Laser Renewal Clinic to simply "Brisa Laser Clinic' and need this logo changed to reflect same

Brisa Laser Clinic
Est. 2004

I also need new business cards with above logo included and this attached card changed to the following.
Marcia Pellbrook
Dermal Aesthetician
Grad Cert in Laser & IPL Treatments

I need at least one logo in less than 4mb so I can upload into my newsletter format so I can upload to newsletters, emails etc

Thanks
Marcie

```html
<!DOCTYPE html>
<html lang="en">
<head>
<meta charset="utf-8">
<title>Brisa Laser Clinic – Business Card</title>
<link href="https://fonts.googleapis.com/css2?family=Lato:wght@400;700&family=Oswald:wght@400;700&display=swap" rel="stylesheet">
<style>
  :root {
    --page-bg: #e6e7e9;
    --card-green: #0f9d58;
    --band-grey: #3b3b3d;
    --ink-white: #ffffff;
  }
  * { margin: 0; padding: 0; box-sizing: border-box; }
  html, body {
    width: 1200px; height: 864px; overflow: hidden;
    background: var(--page-bg);
  }
  .business-card {
    position: absolute;
    left: 80px; top: 114px;
    width: 1040px; height: 636px;
    background: var(--card-green);
    box-shadow: 0 12px 30px rgba(0,0,0,0.18);
    overflow: hidden;
    color: var(--ink-white);
    font-family: "Lato", sans-serif;
  }
  .card-lines { position: absolute; inset: 0; }
  .role-title {
    position: absolute; right: 90px; top: 62px;
    font-size: 20px; font-weight: 700; letter-spacing: 0.3px;
  }
  .holder-name {
    position: absolute; left: 62px; top: 100px;
    font-family: "Oswald", sans-serif;
    font-size: 32px; letter-spacing: 0.5px; text-transform: uppercase;
  }
  .holder-name .first { font-weight: 700; }
  .holder-name .last { font-weight: 400; }
  .brand-mark {
    position: absolute; left: 86px; top: 270px;
    display: flex; align-items: center; gap: 16px;
    font-size: 72px; font-weight: 700; line-height: 1;
  }
  .brand-dot {
    width: 22px; height: 22px; border-radius: 50%;
    background: var(--ink-white);
  }
  .qualification {
    position: absolute; left: 86px; top: 380px;
    font-size: 23px; font-weight: 400;
  }
  .clinic-block { position: absolute; left: 500px; top: 180px; }
  .clinic-name {
    font-size: 32px; font-weight: 700; letter-spacing: 1.5px;
    line-height: 1;
  }
  .clinic-est {
    font-size: 16px; font-weight: 400; letter-spacing: 2px; margin-top: 6px;
  }
  .contact-list { list-style: none; margin-top: 26px; margin-left: 8px; }
  .contact-list li { font-size: 18px; font-weight: 700; }
  .contact-list .address { margin-bottom: 24px; }
  .contact-list .phone { margin-bottom: 32px; }
  .contact-list .email { margin-bottom: 6px; }
</style>
</head>
<body>
  <article class="business-card">
    <svg class="card-lines" width="1040" height="636" viewBox="0 0 1040 636" aria-hidden="true">
      <path d="M560 60 L1040 60 L1040 104 L640 104 Q612 104 598 130 Q588 150 560 150 Z" fill="var(--band-grey)"/>
      <path d="M0 150 L560 150 Q588 150 598 130 Q612 104 640 104 L1040 104" fill="none" stroke="var(--ink-white)" stroke-width="5"/>
      <line x1="560" y1="57" x2="1040" y2="57" stroke="var(--ink-white)" stroke-width="4"/>
      <rect x="0" y="520" width="1040" height="30" fill="var(--band-grey)"/>
      <rect x="0" y="555" width="1040" height="5" fill="var(--ink-white)"/>
      <rect x="0" y="586" width="1040" height="14" fill="var(--band-grey)"/>
      <rect x="0" y="603" width="1040" height="3" fill="var(--ink-white)"/>
    </svg>

    <div class="role-title">Dermal Aesthetician</div>
    <h1 class="holder-name"><span class="first">Marcia</span> <span class="last">Pellbrook</span></h1>

    <div class="brand-mark"><span class="brand-dot" aria-hidden="true"></span><span>Brisa</span></div>
    <p class="qualification">Grad Cert in Laser &amp; IPL Treatments</p>

    <section class="clinic-block">
      <h2 class="clinic-name">Brisa Laser Clinic</h2>
      <p class="clinic-est">Est. 2004</p>
      <ul class="contact-list">
        <li class="address">48 Tarrow Street Kelbury SA 5091</li>
        <li class="phone">(08) 7402 1935</li>
        <li class="email">hello@brisaclinic.com.au</li>
        <li class="web">www.brisaclinic.com.au</li>
      </ul>
    </section>
  </article>
</body>
</html>
```